M Zyvantics Buisness Cards

I need a technology focused clean business card for my employees. I have attached out logo to include in the mocks. We're a modern tech consulting firm that drives to interface humanity with technology in a truly cohesive fashion.

```html
<!DOCTYPE html>
<html lang="en">
<head>
<meta charset="utf-8">
<title>M Zyvantics Business Cards</title>
<link rel="stylesheet" href="https://fonts.googleapis.com/css2?family=Montserrat:wght@300;400;600;700&display=swap">
<style>
  :root {
    --bg: #2b2d31;
    --card-white: #ffffff;
    --card-black: #2a2a2c;
    --blue: #1f74c4;
    --ink: #1d1d1f;
    --grey: #85878b;
    --grey-soft: #b9babd;
    --icon-box: #2c2d30;
    --icon-line: #3a8fe0;
  }
  * { margin: 0; padding: 0; box-sizing: border-box; }
  html, body {
    width: 1200px; height: 900px; overflow: hidden;
    background: var(--bg);
    font-family: "Montserrat", sans-serif;
  }
  .canvas {
    width: 1200px; height: 900px;
    display: flex; flex-direction: column; align-items: center; justify-content: center;
    gap: 60px;
  }
  .card {
    position: relative;
    width: 560px; height: 320px;
    border-radius: 24px;
    overflow: hidden;
    box-shadow: 0 18px 40px rgba(0,0,0,0.35);
  }

  /* front */
  .card--front { background: var(--card-white); }
  .identity {
    position: absolute; left: 40px; top: 34px;
    padding-left: 12px;
    border-left: 4px solid var(--blue);
  }
  .identity__name { font-weight: 700; font-size: 22px; color: var(--ink); letter-spacing: -0.3px; line-height: 1.05; }
  .identity__title { font-weight: 300; font-size: 14px; color: var(--blue); letter-spacing: 0.5px; }

  .contact-row { position: absolute; left: 0; height: 50px; display: flex; align-items: stretch; }
  .contact-row--phone { top: 106px; }
  .contact-row--web { top: 164px; }
  .contact-row--address { top: 222px; }
  .contact-row__band {
    width: 300px;
    background: var(--blue);
    clip-path: polygon(0 0, 100% 0, 88% 100%, 0 100%);
    color: #fff; font-size: 11.5px; font-weight: 400;
    padding: 8px 0 0 32px; line-height: 1.5;
    white-space: nowrap;
  }
  .contact-row--address .contact-row__band { padding-top: 16px; }
  .contact-row__icon {
    width: 44px; margin-left: -24px;
    background: var(--icon-box);
    clip-path: polygon(40% 0, 100% 0, 60% 100%, 0 100%);
    display: flex; align-items: center; justify-content: center;
  }
  .contact-row__icon svg { width: 14px; height: 14px; }

  .brand { display: flex; align-items: center; gap: 12px; }
  .brand__dot { width: 18px; height: 18px; border-radius: 50%; background: var(--blue); flex: none; }
  .brand__name { font-weight: 600; color: var(--grey); letter-spacing: 1px; white-space: nowrap; }
  .card--front .brand { position: absolute; left: 342px; top: 142px; }
  .card--front .brand__name { font-size: 24px; }

  /* back */
  .card--back {
    background: var(--card-black);
    display: flex; flex-direction: column; align-items: center; justify-content: center;
    gap: 22px;
  }
  .card--back .brand__name { font-size: 38px; }
  .card--back .brand__dot { width: 24px; height: 24px; }
  .web-line { font-size: 13px; color: var(--grey-soft); letter-spacing: 3px; font-weight: 400; }
</style>
</head>
<body>
<main class="canvas">
  <section class="card card--front" aria-label="Business card front">
    <div class="identity">
      <p class="identity__name">YOUR NAME</p>
      <p class="identity__title">JOB TITLE</p>
    </div>

    <div class="contact-row contact-row--phone">
      <div class="contact-row__band">000 000 0000<br>000 000 0000(CELL)</div>
      <div class="contact-row__icon">
        <svg viewBox="0 0 24 24" fill="none" stroke="var(--icon-line)" stroke-width="2"><path d="M5 3h4l2 5-3 2a11 11 0 0 0 6 6l2-3 5 2v4a2 2 0 0 1-2 2A18 18 0 0 1 3 5a2 2 0 0 1 2-2z"/></svg>
      </div>
    </div>

    <div class="contact-row contact-row--web">
      <div class="contact-row__band">www.yourwebsite.com<br>youremail@xyz.com</div>
      <div class="contact-row__icon">
        <svg viewBox="0 0 24 24" fill="none" stroke="var(--icon-line)" stroke-width="2"><circle cx="12" cy="12" r="9"/><path d="M3 12h18M12 3c3 3 3 15 0 18M12 3c-3 3-3 15 0 18"/></svg>
      </div>
    </div>

    <div class="contact-row contact-row--address">
      <div class="contact-row__band">000, Street Name, City Name, ST 0000</div>
      <div class="contact-row__icon">
        <svg viewBox="0 0 24 24" fill="none" stroke="var(--icon-line)" stroke-width="2"><path d="M12 22s7-7 7-12a7 7 0 0 0-14 0c0 5 7 12 7 12z"/><circle cx="12" cy="10" r="2.5"/></svg>
      </div>
    </div>

    <div class="brand">
      <span class="brand__dot"></span>
      <span class="brand__name">M Zyvantics</span>
    </div>
  </section>

  <section class="card card--back" aria-label="Business card back">
    <div class="brand">
      <span class="brand__dot"></span>
      <span class="brand__name">M Zyvantics</span>
    </div>
    <p class="web-line">www.yourwebsite.com</p>
  </section>
</main>
</body>
</html>
```